Website design for commercial and residential security company

we're looking to see some new designs for an established company with no website.

homepage and one inner page

here is a link to the homepage content, sitemap, logo and more.
https://files.trovelink-share.net/folders/7QmzKpw3RtvxnLa9eHs2YcdJfuoPb?view=open

call to action should be Request A Quote

if you have any questions please send them to us asap

thank you

Number of Pages Required

1 page

Font styles to use
Sans Serif

```html
<!DOCTYPE html>
<html lang="en">
<head>
<meta charset="utf-8">
<title>Beacon Watch Security</title>
<link href="https://fonts.googleapis.com/css2?family=Raleway:wght@400;600;700;800&family=Open+Sans:wght@400;600&display=swap" rel="stylesheet">
<style>
:root{
  --gold:#d8a91f;
  --ink:#1d1d1d;
  --text:#555;
  --dark:#1c1c1c;
  --footer:#1f1f1f;
  --line:#e4e4e4;
  --white:#fff;
}
*{box-sizing:border-box;margin:0;padding:0}
html,body{width:1200px;height:3072px;overflow:hidden}
body{position:relative;background:var(--white);font-family:"Open Sans",sans-serif;color:var(--text);font-size:13px;line-height:1.6}
h1,h2,h3,h4,.brand,.nav,.btn{font-family:"Raleway",sans-serif}
.abs{position:absolute}
.btn{display:inline-block;background:var(--gold);color:var(--white);font-size:11px;font-weight:700;letter-spacing:.5px;padding:10px 22px;text-transform:uppercase}

/* top bar & header */
.topbar{left:0;top:0;width:1200px;height:32px;background:var(--dark)}
.topbar .phone{position:absolute;right:112px;top:7px;color:var(--gold);font-size:12px;font-weight:600;display:flex;gap:8px;align-items:center}
.header{left:0;top:32px;width:1200px;height:68px;background:var(--white)}
.brand{position:absolute;left:112px;top:20px;display:flex;align-items:center;gap:10px;color:var(--gold);font-weight:800;font-size:22px;letter-spacing:1px}
.brand i{width:22px;height:22px;background:var(--gold);display:block}
.nav{position:absolute;right:112px;top:24px;display:flex;gap:44px;font-size:13px;color:var(--ink)}
.nav .active{color:var(--gold)}

/* hero */
.hero{left:0;top:100px;width:1200px;height:448px;background:linear-gradient(100deg,#2a2a2a 0%,#5a5a5a 45%,#8b8b8b 60%,#3c3c3c 100%)}
.hero-copy{left:112px;top:250px;color:var(--white)}
.hero-copy .pre{font-family:"Raleway",sans-serif;font-size:18px}
.hero-copy h1{font-size:38px;font-weight:800;line-height:1.1;text-transform:uppercase}
.hero-copy h1 span{color:var(--gold)}
.hero-copy p{font-size:13px;margin:6px 0 26px}

/* services & about */
.service{width:220px}
.service svg{display:block;margin-bottom:6px}
.service h4{font-size:16px;font-weight:600;color:var(--ink)}
.service p{font-size:11px;line-height:1.5}
.about{left:652px;top:676px;width:436px}
.about h2{font-size:34px;font-weight:800;color:var(--ink);margin-bottom:12px}
.about p{margin-bottom:14px}

/* solution */
.section-title{left:0;width:1200px;text-align:center;font-size:34px;font-weight:800;color:var(--ink)}
.photo{background:linear-gradient(135deg,#4b4b4b,#a8a8a8)}
.solution-text{width:476px}
.solution-text h3{font-size:24px;font-weight:600;color:var(--ink);margin-bottom:10px}
.solution-text ul{list-style:none;margin:12px 0 22px;font-size:10px;text-transform:uppercase;color:var(--ink)}
.solution-text li::before{content:"";display:inline-block;width:5px;height:5px;background:var(--gold);border-radius:50%;margin-right:8px;vertical-align:middle}

/* newsletter */
.newsletter{left:0;top:1860px;width:1200px;height:300px;background:linear-gradient(90deg,#1e1e1e 0%,#3b3b3b 55%,#8a8a8a 80%,#4a4a4a 100%)}
.newsletter-copy{left:112px;top:1936px;color:var(--white)}
.newsletter-copy .pre{font-family:"Raleway",sans-serif;font-size:20px;font-weight:600}
.newsletter-copy h2{font-size:34px;font-weight:800;line-height:1.1}
.subscribe{left:112px;top:2040px;display:flex}
.subscribe .field{width:320px;height:40px;background:var(--white);font-size:11px;color:#999;padding:11px 14px}
.subscribe .btn{height:40px;padding:13px 22px;margin-left:8px}

/* blog */
.card{width:308px;top:2280px}
.card .thumb{height:200px;background:linear-gradient(135deg,#d9d3cb,#8d8780)}
.card .date{font-size:10px;color:var(--ink);margin:14px 0 6px;font-weight:600}
.card h4{font-size:16px;font-weight:600;color:var(--ink);line-height:1.3;margin-bottom:8px}
.card p{font-size:10px;line-height:1.5;margin-bottom:20px}

/* footer */
.footer{left:0;top:2740px;width:1200px;height:332px;background:var(--footer);color:#bbb}
.fcol{top:2790px;font-size:11px;line-height:2}
.fcol h4{font-size:16px;font-weight:600;color:var(--white);margin-bottom:10px}
.fcol .row{display:flex;gap:10px;align-items:flex-start;line-height:1.6;margin-bottom:12px}
.dot{width:14px;height:14px;border-radius:50%;background:var(--gold);flex:none;margin-top:2px}
.copyright{left:0;top:3020px;width:1200px;border-top:1px solid #333;padding-top:16px;text-align:center;font-size:10px;color:#bbb;letter-spacing:.5px}
.copyright span{color:var(--gold)}
</style>
</head>
<body>

<div class="abs topbar">
  <div class="phone">
    <svg width="12" height="12" viewBox="0 0 24 24"><path fill="#d8a91f" d="M6.6 10.8a15 15 0 006.6 6.6l2.2-2.2c.3-.3.7-.4 1-.2 1.1.4 2.3.6 3.6.6.6 0 1 .4 1 1V20c0 .6-.4 1-1 1A17 17 0 013 4c0-.6.4-1 1-1h3.5c.6 0 1 .4 1 1 0 1.3.2 2.5.6 3.6.1.3 0 .7-.2 1z"/></svg>
    (555) 018-2740
  </div>
</div>

<header class="abs header">
  <div class="brand"><i></i>BEACON WATCH</div>
  <nav class="nav"><span class="active">Home</span><span>About</span><span>Solution</span><span>Process</span><span>Contact</span></nav>
</header>

<section class="abs hero" role="img" aria-label="Photo of a security dome camera on a wall with a white indoor camera in front"></section>
<div class="abs hero-copy">
  <div class="pre">We Offer</div>
  <h1>Monitoring <span>Services</span></h1>
  <p>For both Residential and Commercial systems</p>
  <span class="btn">Read More</span>
</div>

<div class="abs service" style="left:112px;top:572px">
  <svg width="44" height="36" viewBox="0 0 44 36"><rect x="6" y="6" width="26" height="12" rx="2" fill="#4a6fa5"/><rect x="30" y="9" width="8" height="6" fill="#2f4f7a"/><rect x="14" y="18" width="4" height="10" fill="#888"/><rect x="8" y="28" width="16" height="3" fill="#888"/></svg>
  <h4>CCTV</h4>
  <p>Round the clock camera cover for every site.</p>
</div>
<div class="abs service" style="left:360px;top:572px">
  <svg width="44" height="36" viewBox="0 0 44 36"><circle cx="20" cy="18" r="15" fill="#3b8fd9"/><path d="M5 18h30M20 3v30M10 8c6 4 14 4 20 0M10 28c6-4 14-4 20 0" stroke="#fff" stroke-width="1.5" fill="none"/><circle cx="34" cy="26" r="6" fill="#d8a91f"/></svg>
  <h4>Access Control</h4>
  <p>Smart entry systems for doors and gates.</p>
</div>
<div class="abs service" style="left:112px;top:820px">
  <svg width="44" height="36" viewBox="0 0 44 36"><path d="M10 28V18a10 10 0 0120 0v10z" fill="#e0452f"/><rect x="6" y="28" width="28" height="5" fill="#555"/><path d="M20 2v5M5 9l4 3M35 9l-4 3" stroke="#e0452f" stroke-width="2"/></svg>
  <h4>Alarm</h4>
  <p>Fast alerts the moment anything moves.</p>
</div>
<div class="abs service" style="left:360px;top:820px">
  <svg width="44" height="36" viewBox="0 0 44 36"><rect x="4" y="4" width="32" height="22" rx="2" fill="#e8a33a"/><rect x="7" y="7" width="26" height="16" fill="#c0392b"/><rect x="16" y="26" width="8" height="4" fill="#777"/><rect x="10" y="30" width="20" height="3" fill="#777"/></svg>
  <h4>Audio / Video</h4>
  <p>Clear sound and picture in every room.</p>
</div>

<div class="abs about">
  <h2>ABOUT US</h2>
  <p>We protect homes and businesses with trusted systems, careful installs and local support. Our team plans each setup around the way you live and work every day.</p>
  <p>From a single camera to a full site, we keep watch so you can rest easy. Ask our experts and get a plan built for your needs today.</p>
  <span class="btn">Read More</span>
</div>

<h2 class="abs section-title" style="top:1000px">OUR SOLUTION</h2>

<div class="abs photo" style="left:112px;top:1072px;width:480px;height:320px" role="img" aria-label="Photo of a white security camera mounted on a building wall"></div>
<div class="abs solution-text" style="left:612px;top:1072px">
  <h3>Commercial Business</h3>
  <p>Keep your staff, stock and premises safe with systems sized for your site. We design, install and monitor so your business stays open and secure, day and night, all year round.</p>
  <ul><li>CCTV</li><li>Access Control</li><li>Alarm</li><li>Audio / Video</li></ul>
  <span class="btn">Read More</span>
</div>

<div class="abs solution-text" style="left:112px;top:1490px">
  <h3>Residential Business</h3>
  <p>Give your family peace of mind with simple, smart home security. We set up cameras, alarms and automation that work together and are easy to use from your phone anywhere.</p>
  <ul><li>CCTV</li><li>Alarm</li><li>Home</li><li>Automation</li><li>Audio Video</li></ul>
  <span class="btn">Read More</span>
</div>
<div class="abs photo" style="left:612px;top:1480px;width:476px;height:320px;background:linear-gradient(135deg,#e9e6e2,#b8b2aa)" role="img" aria-label="Photo of a hand pressing a wall mounted alarm keypad"></div>

<section class="abs newsletter" role="img" aria-label="Photo of a smart home speaker on a table in a dim living room"></section>
<div class="abs newsletter-copy">
  <div class="pre">Subscribe To</div>
  <h2>OUR NEWSLETTER</h2>
</div>
<div class="abs subscribe"><div class="field">Your email</div><span class="btn">Sign Up</span></div>

<h2 class="abs section-title" style="top:2200px">BLOG POST</h2>

<article class="abs card" style="left:112px">
  <div class="thumb" role="img" aria-label="Photo of a small white smart camera on a shelf"></div>
  <div class="date">12TH MAY 2021</div>
  <h4>Expound the actual teachings of the great explorer</h4>
  <p>Simple tips to choose the right camera for your home and where to place it for the best view.</p>
  <span class="btn">Read More</span>
</article>
<article class="abs card" style="left:446px">
  <div class="thumb" role="img" aria-label="Photo of a technician fitting a ceiling smoke sensor" style="background:linear-gradient(135deg,#e6e2dc,#9b948b)"></div>
  <div class="date">12TH MAY 2021</div>
  <h4>Expound the actual teachings of the great explorer</h4>
  <p>How a planned install saves time and money, and what to expect on the day we visit.</p>
  <span class="btn">Read More</span>
</article>
<article class="abs card" style="left:780px">
  <div class="thumb" role="img" aria-label="Photo of a person using a wall security panel at home" style="background:linear-gradient(135deg,#d7c2a8,#7c8a96)"></div>
  <div class="date">12TH MAY 2021</div>
  <h4>Expound the actual teachings of the great explorer</h4>
  <p>Why a linked alarm and access system keeps your family safe while you are away.</p>
  <span class="btn">Read More</span>
</article>

<footer class="abs footer"></footer>
<div class="abs fcol" style="left:112px"><h4>Sitemap</h4>Home<br>About Us<br>Solution<br>Process<br>Contact Us</div>
<div class="abs fcol" style="left:290px"><h4>Commercial</h4>CCTV<br>Access<br>Control<br>Alarm<br>Audio / Video</div>
<div class="abs fcol" style="left:510px"><h4>Residential</h4>CCTV<br>Alarm<br>Home Automation<br>Audio Video<br>Network WiFi</div>
<div class="abs fcol" style="left:710px;width:220px">
  <h4>Contact Us</h4>
  <div class="row"><span class="dot"></span>214 Harbor Row, Suite 8, Fairmont</div>
  <div class="row"><span class="dot"></span>(555) 018-2740</div>
  <div class="row"><span class="dot"></span>hello@beaconwatch.example</div>
</div>
<div class="abs fcol" style="left:986px">
  <h4>Follow Us</h4>
  <div class="row"><span class="dot"></span>Community</div>
  <div class="row"><span class="dot"></span>Updates</div>
  <div class="row"><span class="dot"></span>Gallery</div>
</div>
<div class="abs copyright">COPYRIGHT © 2021 <span>BEACON WATCH SECURITY</span>. ALL RIGHTS RESERVED.</div>

</body>
</html>
```